Lorvenna vineyards

Wine label/logo that is old world witH a modern Maybe Latin/Hispanic twist. Nothing cartoonish or colorful.
Updates

This is a wine vineyard growing tempranillo, Malbec, cabarnet. I am looking for a wine label that incorporates the logo for Lorvenna Vineyards. Location Temecula california

```html
<!DOCTYPE html>
<html lang="en">
<head>
<meta charset="utf-8">
<title>Lorvenna Vineyards — Malbec Label</title>
<link rel="stylesheet" href="https://fonts.googleapis.com/css2?family=Cinzel:wght@400&family=Cormorant+Garamond:wght@500&display=swap">
<style>
  :root {
    --backdrop: #e6dfcf;
    --slate: #1e1f22;
    --slate-light: #2a2b2f;
    --gold: #d6aa4c;
    --gold-soft: rgba(214, 170, 76, 0);
  }
  * { box-sizing: border-box; margin: 0; padding: 0; }
  html, body {
    width: 1200px;
    height: 909px;
    overflow: hidden;
    background: var(--backdrop);
  }
  .wine-label {
    position: absolute;
    left: 311px;
    top: 44px;
    width: 577px;
    height: 820px;
    background: radial-gradient(ellipse at 40% 35%, var(--slate-light), var(--slate) 75%);
    color: var(--gold);
    text-align: center;
  }
  .label-frame {
    position: absolute;
    left: 13px;
    top: 16px;
    right: 13px;
    bottom: 15px;
    border: 1.5px solid var(--gold);
  }
  .label-text {
    position: absolute;
    left: 0;
    width: 100%;
    line-height: 1;
    white-space: nowrap;
  }
  .brand-name {
    font-family: "Cinzel", serif;
    font-weight: 400;
    color: var(--gold);
  }
  .brand-name .brand-main {
    top: 286px;
    font-size: 84px;
    letter-spacing: 1px;
  }
  .brand-name .brand-sub {
    top: 369px;
    font-size: 34px;
    letter-spacing: 5px;
  }
  .varietal-rule {
    position: absolute;
    left: 181px;
    width: 215px;
    height: 1.5px;
    background: linear-gradient(90deg, var(--gold-soft), var(--gold) 20%, var(--gold) 80%, var(--gold-soft));
  }
  .varietal-rule.top { top: 533px; }
  .varietal-rule.bottom { top: 570px; }
  .varietal {
    top: 539px;
    font-family: "Cinzel", serif;
    font-size: 27px;
    letter-spacing: 1px;
  }
  .vintage {
    top: 584px;
    font-family: "Cormorant Garamond", serif;
    font-weight: 500;
    font-size: 32px;
  }
  .appellation {
    top: 714px;
    font-family: "Cinzel", serif;
    font-size: 26px;
    letter-spacing: 1.5px;
  }
</style>
</head>
<body>
  <main class="wine-label">
    <div class="label-frame"></div>

    <div class="brand-name">
      <div class="label-text brand-main">LORVENNA</div>
      <div class="label-text brand-sub">VINEYARDS</div>
    </div>

    <div class="varietal-rule top"></div>
    <div class="label-text varietal">MALBEC</div>
    <div class="varietal-rule bottom"></div>
    <div class="label-text vintage">2020</div>

    <div class="label-text appellation">Temecula Valley, California</div>
  </main>
</body>
</html>
```